Book cover for book about ex-wifes

I need a book cover for my new book called "Naboer fra Bakken, Mosen og Tjørnelunde" - In english: "Neighbours from Hilltop, Marsh and Tjørnelunde" (Hørsholm is a posh city in Denmark).

The book is by men for men about ex-wifes and about how to avoid getting them.
Is it a book from a sexologist and couples therapist to men on how to improve relations.

Target Market(s)

Men (and curious women)

Requirements
Must have
• Something that indicate three types of ex-wifes

And the author name “Jonas Birkvig”
Nice to have
• Something that says something about relationships, couples and how to stay together (or how to avoid not breaking up)
Should not have
• No hate

```html
<!DOCTYPE html>
<html lang="da">
<head>
<meta charset="utf-8">
<title>Naboer fra Bakken, Mosen og Tjørnelunde – Jonas Birkvig</title>
<link rel="stylesheet" href="https://fonts.googleapis.com/css2?family=Oswald:wght@200;300;700&display=swap">
<style>
  :root {
    --backdrop: #e4e4e4;
    --maroon: #5b2a2c;
    --maroon-deep: #3a1c1f;
    --maroon-dark: #2c1517;
    --photo-light: #f2efec;
    --photo-skin: #d9b79c;
    --photo-hair: #c9a27a;
    --ink-white: #ffffff;
  }
  * { margin: 0; padding: 0; box-sizing: border-box; }
  html, body {
    width: 1200px;
    height: 857px;
    overflow: hidden;
    background: var(--backdrop);
  }
  .stage {
    width: 1200px;
    height: 857px;
    display: flex;
    align-items: center;
    justify-content: center;
  }
  .cover {
    position: relative;
    width: 540px;
    height: 790px;
    overflow: hidden;
    background:
      radial-gradient(ellipse at 75% 70%, var(--maroon-dark) 0%, transparent 60%),
      linear-gradient(180deg, var(--maroon) 0%, var(--maroon-deep) 100%);
    box-shadow: 0 6px 24px rgba(0,0,0,0.18);
  }
  .cover-photo {
    position: absolute;
    inset: 0 0 auto 0;
    height: 470px;
    background:
      radial-gradient(ellipse 22% 40% at 20% 30%, var(--photo-hair) 0%, transparent 70%),
      radial-gradient(ellipse 18% 36% at 52% 25%, var(--photo-skin) 0%, transparent 70%),
      radial-gradient(ellipse 18% 36% at 82% 25%, var(--photo-skin) 0%, transparent 70%),
      linear-gradient(180deg, var(--photo-light) 0%, #e6d3c4 55%, rgba(91,42,44,0) 100%);
  }
  .cover-photo::after {
    content: "";
    position: absolute;
    inset: 0;
    background: linear-gradient(180deg, rgba(91,42,44,0) 45%, var(--maroon) 100%);
  }
  .title {
    position: absolute;
    left: 40px;
    right: 26px;
    top: 372px;
    color: var(--ink-white);
    font-family: "Oswald", sans-serif;
    text-transform: uppercase;
  }
  .title-main {
    display: block;
    font-weight: 700;
    font-size: 112px;
    line-height: 0.98;
    letter-spacing: 1px;
  }
  .title-sub {
    display: block;
    font-weight: 700;
    font-size: 47px;
    line-height: 1.02;
    letter-spacing: 0.5px;
  }
  .title-thin {
    display: block;
    font-weight: 200;
    font-size: 56px;
    line-height: 1.05;
    letter-spacing: 1px;
  }
  .author {
    position: absolute;
    left: 0;
    right: 0;
    bottom: 66px;
    text-align: center;
    color: var(--ink-white);
    font-family: "Oswald", sans-serif;
    font-weight: 200;
    font-size: 36px;
    letter-spacing: 1px;
    text-transform: uppercase;
  }
</style>
</head>
<body>
  <main class="stage">
    <article class="cover">
      <div class="cover-photo" role="img" aria-label="Soft-focus photograph of three women with long hair, side by side, blurred as if in motion"></div>
      <h1 class="title">
        <span class="title-main">Naboer</span>
        <span class="title-sub">fra Bakken, Mosen</span>
        <span class="title-thin">og Tjørnelunde</span>
      </h1>
      <p class="author">Jonas Birkvig</p>
    </article>
  </main>
</body>
</html>
```